New Professional Business Web Site

We need a web design for an existing company based in Dallas called "FinchLoop".
We provide software and professional services to enterprise customers in the contact centre space. We have a global customer base but primarily US and UK.
Our initial products are as follows-
LineSight - an application that helps Torvane contact centre managers and administrators observe individual calls in queue.
MassLoad - an application that allows Torvane administrators to load large groups of extensions and associate them to places.
ClustR - an application that helps Torvane customers manage multilayers of agent and place groups into hiearchical and geographical groups of groups.
We would like to see designs that use the colors black, gray, and red as this matches with our new logo we have had designed from this web site and will have available in a few days.
The final design should communicate professionalism, innovation, software, large corporation, and telecommunications.
We're looking to provide features like-
1) Interactive Support Portal for customers
2) Product Descriptions
3) Product Purchasing
4) Interactive Forum
Target Market(s)
enterprise companies interested in call center related products and services
Industry/Entity Type
Business
Look and feel

```html
<!DOCTYPE html>
<html lang="en">
<head>
<meta charset="utf-8">
<title>FinchLoop – Contact Centre Software</title>
<link rel="stylesheet" href="https://fonts.googleapis.com/css2?family=Arimo:wght@400;700&family=Cinzel:wght@600&family=PT+Sans:wght@400;700&display=swap">
<style>
:root{
  --page-top:#3e3f44;
  --page:#585b66;
  --white:#ffffff;
  --ink:#222222;
  --body-text:#3a3a3a;
  --red:#d8222a;
  --red-dark:#a5141a;
  --tab:#5d8597;
  --hero-bg:#f2f2f2;
  --col-a:#3e3e3e;
  --col-b:#222222;
  --col-c:#6a6a6a;
  --col-text:#d6d6d6;
  --orange:#f0902a;
  --box-bg:#f3f3ef;
  --box-line:#a9a9a9;
  --footer-text:#dcdcdc;
}
*{margin:0;padding:0;box-sizing:border-box}
html,body{width:1053px;height:1200px;overflow:hidden}
body{position:relative;background:linear-gradient(var(--page-top) 0 118px,var(--page) 118px);font-family:"Arimo",Arial,sans-serif;color:var(--body-text)}
.abs{position:absolute}
.site{position:absolute;left:110px;top:29px;width:835px;height:1084px;background:var(--white)}
.brand{left:133px;top:58px;display:flex;align-items:center;gap:10px;font-family:"PT Sans",sans-serif;font-weight:700;font-size:30px;color:var(--ink)}
.brand-dot{width:30px;height:30px;border-radius:50%;background:var(--red)}
.account{right:128px;top:70px;font-size:10px;color:#333;word-spacing:0}
.account span{margin:0 14px}
.nav{left:110px;top:134px;width:835px;height:43px;background:linear-gradient(var(--red),var(--red-dark))}
.nav a{position:absolute;top:0;height:43px;line-height:40px;color:var(--white);font-size:12.5px;text-decoration:none}
.nav .current{left:8px;width:80px;background:var(--tab);text-align:center}
.hero-wrap{left:110px;top:177px;width:835px;height:333px;background:var(--hero-bg)}
.hero-photo{left:129px;top:192px;width:792px;height:299px;background:linear-gradient(90deg,#e9e9e9 0%,#e4e1dc 40%,#d8c3ad 65%,#c9a779 85%,#e3e1dc 100%)}
.hero-title{left:150px;top:262px;font-family:"PT Sans",sans-serif;font-size:25px;line-height:35px;color:#333}
.hero-title span{display:block}
.hero-title span:first-child{padding-left:10px}
.hero-text{left:149px;top:344px;width:340px;font-size:14px;line-height:26.5px;color:#333}
.dots{left:392px;top:462px;display:flex;gap:1px}
.dots i{width:18px;height:18px;border-radius:50%;background:var(--tab)}
.dots i:first-child{background:var(--red)}
.product{top:510px;height:264px}
.product h2{position:absolute;top:10px;left:0;right:0;text-align:center;font-family:"Cinzel",serif;font-weight:600;font-size:20px;color:var(--white)}
.product .shot{position:absolute;top:50px;height:142px;width:242px}
.product p{position:absolute;top:201px;font-size:12px;line-height:19px;color:var(--col-text)}
.product .more{position:absolute;top:241px;font-size:12px;color:var(--orange)}
.more small{font-size:9px;margin-right:6px}
.p1{left:110px;width:269px;background:var(--col-a)}
.p2{left:379px;width:287px;background:var(--col-b)}
.p3{left:666px;width:279px;background:var(--col-c)}
.article h1{font-family:"PT Sans",sans-serif;font-weight:400;font-size:23px;color:var(--ink)}
.article h1 em{font-style:normal;color:var(--red)}
.article h2{font-family:"PT Sans",sans-serif;font-weight:400;font-size:20px;color:var(--ink)}
.article p{font-size:12px;line-height:21px;color:#333;width:530px}
.red-more{font-size:12px;color:var(--red)}
.divider{left:119px;top:945px;width:549px;border-top:1px dotted #777}
.box{left:703px;width:232px;background:var(--box-bg);border:1px solid var(--box-line);border-radius:4px}
.box h3{position:absolute;left:0;right:0;text-align:center;font-family:"PT Sans",sans-serif;font-weight:400;font-size:16px;color:var(--ink)}
.field{left:733px;top:832px;width:175px;height:30px;border:1px solid #8a8a8a;background:linear-gradient(#f2f2f2,#b9b9b9)}
.subscribe{left:762px;top:874px;width:96px;height:26px;border-radius:3px;background:linear-gradient(#d32a2e,#a5161b);color:var(--white);font-size:12px;line-height:25px;text-align:center}
.avatar{width:32px;height:32px;border-radius:50%;background:#d4d4d4}
.quote{font-size:9.5px;line-height:12px;color:#333;width:135px}
.quote-more{font-size:9.5px;color:var(--red)}
.social{left:151px;top:1136px;display:flex;gap:12px}
.social i{width:23px;height:23px;border-radius:50%}
.footer-links{left:453px;top:1133px;font-size:11px;color:var(--footer-text)}
.footer-links span{margin:0 12px}
.copyright{left:494px;top:1160px;font-size:11px;color:var(--footer-text)}
</style>
</head>
<body>
<div class="site"></div>

<header>
  <div class="abs brand"><i class="brand-dot"></i>FinchLoop</div>
  <div class="abs account">Register<span>|</span>Sign In<span>|</span>Help</div>
</header>

<nav class="abs nav">
  <a class="current" href="#">HOME</a>
  <a href="#" style="left:98px">ABOUT US</a>
  <a href="#" style="left:194px">IT SUPPORT</a>
  <a href="#" style="left:293px">DEVELOPMENT</a>
  <a href="#" style="left:410px">PRODUCTS</a>
  <a href="#" style="left:505px">CONTACT US</a>
</nav>

<section>
  <div class="abs hero-wrap"></div>
  <div class="abs hero-photo" role="img" aria-label="Photo of a smiling support agent wearing a headset, with a colleague in the background"></div>
  <h1 class="abs hero-title"><span>Interactive Support</span><span>Portal for customers</span></h1>
  <p class="abs hero-text">Lorem ipsum dolor sit amet, consectetuer adipiscing elit. Nam nibh. Nunc varius facilisis eros. Sed erat. Curabitur adipiscing luctus massa.</p>
  <div class="abs dots"><i></i><i></i><i></i><i></i></div>
</section>

<section>
  <div class="abs product p1">
    <h2>LineSight</h2>
    <div class="shot" style="left:15px;background:linear-gradient(120deg,#9fb0c4,#e8e4df 60%,#c9c2ba)" role="img" aria-label="Photo of a call centre agent at a desk with monitors showing call queues"></div>
    <p style="left:19px;width:220px">A software to view call queue by the managers in call centers</p>
    <div class="more" style="left:22px"><small>&gt;&gt;</small>More</div>
  </div>
  <div class="abs product p2">
    <h2>MassLoad</h2>
    <div class="shot" style="left:15px;background:linear-gradient(90deg,#f4f4f4,#d6d6d6 60%,#efefef)" role="img" aria-label="Illustration of headset-wearing figures lined up at laptops"></div>
    <p style="left:26px;width:230px">An application to load up list of numbers to be called for the call center guys</p>
    <div class="more" style="left:26px"><small>&gt;&gt;</small>More</div>
  </div>
  <div class="abs product p3">
    <h2>ClustR</h2>
    <div class="shot" style="left:18px;background:linear-gradient(90deg,#c9ccd3,#d9c3ae 50%,#a9a49f)" role="img" aria-label="Photo of a team of contact centre staff with a headset-wearing agent in front"></div>
    <p style="left:39px;width:225px">software to group up teams and members in the call center</p>
    <div class="more" style="left:39px"><small>&gt;&gt;</small>More</div>
  </div>
</section>

<main class="article">
  <h1 class="abs" style="left:140px;top:787px">Welcome to <em>FinchLoop</em></h1>
  <p class="abs" style="left:141px;top:828px">Lorem ipsum dolor sit amet, adipiscing elit. Nam nibh. Nunc varius facilisis eros. Sed erat.In in velit quis arcuornare laoreet. Curabitur adipiscing luctus massa.Integer ut purus ac commodo commodo. Lorem ipsum dolor sit amet, adipiscing elit. Nam nibh. Nunc varius facilisis eros. Sed erat.In in velit quis arcuornare laoreet. Curabitur adipiscing luctus massa. Integer ut purus ac commodo commodo.</p>
  <div class="abs red-more" style="left:604px;top:919px"><small style="font-size:9px;margin-right:6px">&gt;&gt;</small>More</div>
  <div class="abs divider"></div>
  <h2 class="abs" style="left:146px;top:955px">IT Support &amp; Development</h2>
  <p class="abs" style="left:145px;top:988px">Lorem ipsum dolor sit amet, adipiscing elit. Nam nibh. Nunc varius facilisis eros. Sed erat.In in velit quis arcuornare laoreet. Curabitur adipiscing luctus massa.Integer ut purus ac commodo commodo. Lorem ipsum dolor sit amet, adipiscing elit. Nam nibh. Nunc varius facilisis eros. Sed erat.In in velit quis arcuornare laoreet. Curabitur adipiscing luctus massa. Integer ut purus ac commodo commodo.</p>
  <div class="abs red-more" style="left:616px;top:1088px"><small style="font-size:9px;margin-right:6px">&gt;&gt;</small>More</div>
</main>

<aside>
  <div class="abs box" style="top:787px;height:137px"><h3 style="top:8px">Newsletter</h3></div>
  <div class="abs field"></div>
  <div class="abs subscribe">Subscribe</div>

  <div class="abs box" style="top:937px;height:154px"><h3 style="top:8px">Testimonials</h3></div>
  <div class="abs avatar" style="left:727px;top:980px"></div>
  <p class="abs quote" style="left:775px;top:986px">Lorem ipsum is simply dummy text Lorem Ipsum is simply</p>
  <div class="abs quote-more" style="left:781px;top:1016px">More</div>
  <div class="abs avatar" style="left:727px;top:1033px"></div>
  <p class="abs quote" style="left:775px;top:1040px">Lorem ipsum is simply dummy text Lorem Ipsum is simply</p>
  <div class="abs quote-more" style="left:781px;top:1070px">More</div>
</aside>

<footer>
  <div class="abs social" aria-label="Social links">
    <i style="background:#2a5ea8"></i><i style="background:#43a9dc"></i><i style="background:#2a7ab8"></i><i style="background:#e8762a"></i>
  </div>
  <div class="abs footer-links">Privacy Policy<span>|</span>Terms &amp; Conditions<span>|</span>Contact Us</div>
  <div class="abs copyright">Copyright © FinchLoop , All Rights Reserved</div>
</footer>
</body>
</html>
```